3 Posters for House Designer

I'm installing a set of 3 posters on our office wall to describe the benefits of our house design services. These posters are A0 size and will be seen from the front windows of the office. I have already purchased the AO snap frames to hold the posters, they are silver in colour.

We, Farlow Studio, design houses. We offer Architectural services but as we didn't study Architecture, we're not permitted to use the word Architect or any derivative there of. So no words allowed that say Architect, Architecture or Architectural and the like.

Each poster will highlight a benefit of engaging Farlow Studio to design a house and the posters will be lined up side by side.

The first benefit is GENUINE PASSION.
I am genuinely passionate about designing homes that fit my clients like a glove in every way. I genuinely care about my clients doing the right thing by themselves and I'm not a "yes man". I challenge myself and my clients to ensure the best possible result.

The second benefit is CREATIVE THINKING.
I love a challenge. I can spend hours, even days, working on one small aspect of a house design to make it work best. I love solving design problems on difficult sites. What I pride myself on is delivering house designs which are as great to live with as they are to look at; form and function, beautiful yet practical.

The third benefit is GUARANTEED RESULTS.
My genuine passion and creative thinking result in my initial house designs being 95% right, for my clients, the first time; requiring very few changes. This is why I offer, iron clad, guarantees which form part of our design contract. These guarantees include:
1. Our clients absolutely loving our design. If they want to change something, we'll change it at no additional cost; no matter how big the changes or how many.
2. We guarantee our house designs will be within the given budget to build the house. If not, we'll amend our design at no additional cost.
3. We guarantee our house designs will meet the required minimum 6 star energy efficiency rating. If not, we'll amend the design at no additional cost.
4. We guarantee Council approval to build as designed. If not, we'll amend our design at no additional cost.

I see each benefit title being the hero on each poster (ie GENUINE PASSION). I see white type on a light blue background. I see A hero shot of stylish houses in the backgrounds but blurred. I see life in the posters in the form of colour and happy people (customers). Our customers are aged between 40 & 60.

I have a logo (uploaded) and have already purchased images of people if required. Please advise if you want these.

Check out our website at www.farlow-studio.com.au/Kelmore

Target Market(s)

Couples aged 40 - 60

Industry/Entity Type

House

Requirements
Must have
• Stylish house images, happy people (couples & families), big, bold, hero titles at the top of each of the three posters.

```html
<!DOCTYPE html>
<html lang="en">
<head>
<meta charset="utf-8">
<title>Genuine Passion — Farlow Studio</title>
<link rel="stylesheet" href="https://fonts.googleapis.com/css2?family=Great+Vibes&family=Playfair+Display:wght@900&family=Libre+Baskerville:ital@1&family=Montserrat:wght@400;600&display=swap">
<style>
  :root {
    --navy-deep: #0d2470;
    --navy: #1b3c9c;
    --blue-bright: #2f62c8;
    --white: #ffffff;
    --white-soft: #dfe6f6;
    --sky-low: #3a6cc4;
    --facade: #3a3a42;
    --glow: #f6d08a;
    --glow-hot: #fff1cc;
    --foliage: #1a2a1c;
    --lawn: #27361f;
  }
  html, body {
    margin: 0;
    padding: 0;
    width: 849px;
    height: 1200px;
    overflow: hidden;
    background: var(--white);
  }
  .poster {
    position: relative;
    width: 849px;
    height: 1200px;
    overflow: hidden;
    background: radial-gradient(ellipse at 50% 18%, var(--blue-bright) 0%, var(--navy) 50%, var(--navy-deep) 100%);
  }
  .house-photo {
    position: absolute;
    top: 400px;
    left: 0;
    width: 849px;
    height: 800px;
    background:
      radial-gradient(ellipse 130px 170px at 690px 330px, rgba(255,241,204,0.85) 0%, rgba(246,208,138,0.55) 45%, rgba(246,208,138,0) 100%),
      radial-gradient(ellipse 170px 110px at 230px 480px, rgba(255,241,204,0.8) 0%, rgba(246,208,138,0.5) 50%, rgba(246,208,138,0) 100%),
      radial-gradient(ellipse 200px 90px at 430px 640px, rgba(246,208,138,0.55) 0%, rgba(246,208,138,0) 100%),
      radial-gradient(ellipse 340px 220px at 470px 330px, rgba(40,40,48,0.95) 0%, rgba(40,40,48,0.6) 60%, rgba(40,40,48,0) 100%),
      radial-gradient(ellipse 260px 160px at 300px 700px, rgba(26,42,28,0.95) 0%, rgba(26,42,28,0) 100%),
      radial-gradient(ellipse 200px 300px at 40px 450px, rgba(20,30,22,0.9) 0%, rgba(20,30,22,0) 100%),
      radial-gradient(ellipse 140px 300px at 830px 600px, rgba(20,30,22,0.9) 0%, rgba(20,30,22,0) 100%),
      linear-gradient(180deg, rgba(27,60,156,0) 0%, var(--sky-low) 18%, #2c4f9a 35%, var(--facade) 62%, var(--lawn) 82%, #141c14 100%);
  }
  .hero-title {
    position: absolute;
    top: 58px;
    left: 0;
    width: 100%;
    margin: 0;
    text-align: center;
    color: var(--white);
  }
  .hero-title__script {
    display: block;
    font-family: "Great Vibes", cursive;
    font-weight: 400;
    font-size: 80px;
    line-height: 1;
    margin-bottom: -14px;
  }
  .hero-title__main {
    display: block;
    font-family: "Playfair Display", serif;
    font-weight: 900;
    font-size: 92px;
    letter-spacing: 5px;
    line-height: 1;
    background: repeating-linear-gradient(180deg, var(--white) 0 5px, var(--white-soft) 5px 7px);
    -webkit-background-clip: text;
    background-clip: text;
    color: transparent;
  }
  .statement {
    position: absolute;
    top: 284px;
    left: 60px;
    width: 729px;
    margin: 0;
    text-align: center;
    font-family: "Libre Baskerville", serif;
    font-style: italic;
    font-size: 17px;
    line-height: 1.5;
    color: var(--white);
  }
  .brand {
    position: absolute;
    bottom: 62px;
    left: 0;
    width: 100%;
    text-align: center;
    color: var(--white);
    font-family: "Montserrat", sans-serif;
  }
  .brand__name {
    display: block;
    font-size: 30px;
    font-weight: 600;
    letter-spacing: 0.5px;
  }
  .brand__tagline {
    display: block;
    margin-top: 4px;
    font-size: 8px;
    font-weight: 600;
    letter-spacing: 2px;
    text-transform: uppercase;
  }
</style>
</head>
<body>
  <main class="poster">
    <div class="house-photo" role="img" aria-label="Modern two-storey house at dusk with glowing windows, lawn and trees in front"></div>
    <h1 class="hero-title">
      <span class="hero-title__script">Genuine</span>
      <span class="hero-title__main">PASSION</span>
    </h1>
    <p class="statement">I am genuinely passionate about designing homes that fit my<br>clients like a glove in every way. I genuinely care about my clients<br>doing the right thing by themselves and I'm not a "yes man".<br>I challenge myself and my clients to ensure the best possible result.</p>
    <div class="brand">
      <span class="brand__name">Farlow Studio</span>
      <span class="brand__tagline">Residential home designers Kelmore</span>
    </div>
  </main>
</body>
</html>
```